Hello,
We’re looking for a new WordPress website for Gather Your Light, our company offering unique well-being retreats and workshops.
We currently have a website online (you can consult it : www.gatheryourlight.ch), but we now need to build a new site on WordPress — more flexible, more intuitive to manage, and better aligned with our evolving needs.

What we’re looking for:
A new userfriendly WordPress site, with:
Inspiring, elegant, and modern design
Smooth user experience on desktop and mobile
Innovative design proposals – we want to be inspired !
SEO best practices
Respect of our existing color palette
The final website will need to be set up on our existing hosting provider (details can be shared later)

Pages to Include:
- Home
- Our Story
- Our Stays - with links to 5 individual pages, each describing one of our stays in detail.
- Activities – with potential links to individual descriptive pages
- Agenda
- Our Charter
- The Team
- Contact
- Blog

Required Features:
- Space for photos and videos
- Sections for testimonials and press articles
- Blog/article layout with strong readability
- Easy-to-update backend for future content
- Newsletter sign-up (pop-up and in footer)
- Additional pop-up on/off
- “Request info” buttons
- “Booking request” buttons
- Integration of our 4 pillars - Breathe · Feel · Connect · Experience - in the design (They’re currently in the footer, but we’re open to creative suggestions)

Who we are :
Gather Your Light offers well-being and personal growth stays but with a very different spirit.
We’re not a classic wellness brand. Our approach is professional, joyful, and grounded.
We create spaces where people can take a real break — breathe, slow down, and reconnect with themselves.
During our stays, people are welcomed like friends:
with warmth, respect, and no pressure.
Each program combines practices like breathwork, movement, creativity, coaching, and massages in a relaxed, beautiful setting of the French Alps.
What makes us different:
A friendly and down-to-earth atmosphere
A wide mix of activities.
A mix of inner work and simple pleasures
Private rooms, nourishing food, and shared moments
Time to talk, to laugh, to walk, or just be silent together - and feel free to be yourself
Our guests come to pause.
They leave feeling lighter, aligned, and full of life

```html
<!DOCTYPE html>
<html lang="en">
<head>
<meta charset="utf-8">
<title>Gather Your Light – Well-being Stays</title>
<link href="https://fonts.googleapis.com/css2?family=Poppins:wght@300;400;500;600;700;800&display=swap" rel="stylesheet">
<style>
:root{
  --blue:#1a3d99;
  --blue-dark:#15327f;
  --teal:#5bbfb5;
  --beige:#f0ebe3;
  --ink:#1c1c1c;
  --text:#333;
  --muted:#777;
  --white:#fff;
  --black:#0b0b0b;
  --grey:#e4e4e4;
  --star:#f4c20d;
}
*{box-sizing:border-box;margin:0;padding:0}
html,body{width:1200px;height:4942px;overflow:hidden}
body{font-family:'Poppins',sans-serif;color:var(--text);background:var(--white);position:relative}
.abs{position:absolute}
a{color:inherit;text-decoration:none}

/* top bar */
.topbar{top:0;left:0;width:1200px;height:56px;background:var(--white);border-top:4px solid #eee}
.topbar .info{top:18px;font-size:10px;color:var(--ink);display:flex;align-items:center;gap:6px}
.topbar svg{width:16px;height:16px}
.quote-btn{left:829px;top:3px;width:237px;height:48px;background:var(--blue);color:var(--white);font-weight:600;font-size:17px;display:flex;align-items:center;justify-content:center;border-radius:2px}
.header{top:56px;left:0;width:1200px;height:66px;background:var(--white)}
.logo{left:84px;top:2px;font-size:25px;font-weight:600;color:var(--blue);letter-spacing:1px;line-height:1.1}
.nav{top:22px;right:85px;display:flex;gap:22px;font-size:12px;color:var(--ink);font-weight:500}

/* hero */
.hero{top:122px;left:0;width:1200px;height:640px;background:linear-gradient(180deg,#8fa3c9 0%,#a8b5cf 45%,#8c95a8 75%,#7d8393 100%)}
.hero h1{left:563px;top:100px;width:560px;color:var(--white);font-size:44px;font-weight:800;line-height:1.0;letter-spacing:.3px}
.btn{background:var(--blue);color:var(--white);display:flex;align-items:center;justify-content:center;border-radius:3px}
.hero .btn{left:7px;top:258px;width:235px;height:58px;font-size:22px;position:absolute}
.hero .cta-wrap{left:563px;top:0;position:absolute}

.beige{top:740px;left:0;width:1200px;height:2570px;background:var(--beige)}
.torn{position:absolute;left:0;width:1200px}

.center{left:0;width:1200px;text-align:center}
.h2{font-size:42px;font-weight:500;color:var(--black);letter-spacing:.5px}
.lead{font-size:18px;line-height:29px;color:var(--ink)}
.list{font-size:14.5px;line-height:27.5px;color:var(--ink)}
.photo-wide{left:169px;top:1129px;width:877px;height:407px;border-radius:12px;background:linear-gradient(180deg,#6b6a4e 0%,#a8894a 40%,#3d3420 70%,#1f1b12 100%)}
.small-btn{width:234px;height:57px;font-size:17px;font-weight:500;letter-spacing:.3px}

.pillar{width:457px;height:219px;background:var(--white);border-radius:4px}
.pillar .art{position:absolute;left:12px;top:40px;width:170px;height:145px;border-radius:8px}
.pillar h3{position:absolute;left:186px;top:18px;font-size:37px;font-weight:400;color:var(--blue)}
.pillar .rule{position:absolute;left:188px;top:74px;width:120px;height:2px;background:#ccc}
.pillar p{position:absolute;left:188px;top:96px;width:230px;font-size:11.5px;line-height:17.5px;color:var(--muted)}

.fr{left:80px;width:1040px;text-align:center;font-size:18px;line-height:29px;color:var(--ink)}

/* blog */
.blog{top:3302px;left:0;width:1200px;height:692px;background:var(--blue)}
.blog h2{top:112px;font-size:56px;font-weight:400;color:var(--white)}
.post{top:189px;width:331px;height:391px;background:var(--white);border-radius:3px}
.post .thumb{position:absolute;left:14px;top:17px;width:303px;height:226px}
.post h4{position:absolute;left:10px;top:262px;width:311px;text-align:center;font-size:19px;font-weight:400;line-height:25px;color:#555}
.post .meta{position:absolute;left:0;top:318px;width:331px;text-align:center;font-size:10.5px;color:var(--ink)}
.post .more{position:absolute;left:0;top:340px;width:331px;text-align:center;font-size:18px;color:var(--blue)}

/* testimonial */
.avatar{left:553px;top:4036px;width:88px;height:88px;border-radius:50%;background:radial-gradient(circle at 50% 40%,#e7c9a3,#b99363)}
.tname{font-size:13.5px;font-weight:600;letter-spacing:1px;color:var(--ink)}
.dots{top:4316px;left:563px;display:flex;gap:7px}
.dots span{width:11px;height:11px;border-radius:50%;background:#c7c7c7}
.dots span.on{background:var(--blue)}

/* CTA */
.cta{left:113px;top:4378px;width:970px;height:182px;background:var(--teal);border-radius:14px;text-align:center;color:var(--white);z-index:3}
.cta .phone{margin-top:38px;font-size:52px;font-weight:400;line-height:1.1}
.cta p{font-size:17px;line-height:23px;font-weight:500}

/* footer */
.footer{top:4483px;left:0;width:1200px;height:429px;background:var(--black);color:var(--white)}
.fcol h5{font-size:17px;font-weight:400;color:#6d8fe0;margin-bottom:20px}
.fcol li{list-style:none;font-size:13px;line-height:29px}
.fcontact div{display:flex;gap:14px;align-items:flex-start;font-size:13px;margin-bottom:12px}
.fcontact svg{width:22px;height:22px;flex:none}
.flogo{font-size:34px;font-weight:600;color:#2f5fd0;letter-spacing:1px}
.subscribe{font-size:22px;color:#5f86e3}
.field{width:294px;height:34px;background:var(--white);display:flex;justify-content:flex-end}
.field span{width:100px;height:34px;border-left:2px solid var(--black);font-size:11px;font-weight:600;color:var(--black);display:flex;align-items:center;justify-content:center}
.fine{font-size:9.5px;line-height:13px;font-weight:600;color:var(--white);width:300px}
.quote-tab{left:102px;top:4842px;width:228px;height:73px;background:var(--white);color:var(--black);font-weight:700;font-size:19px;line-height:21px;text-align:center;padding-top:14px;border-radius:3px 3px 0 0;z-index:4}
.bottom{top:4912px;left:0;width:1200px;height:30px;background:var(--grey);font-size:11.5px;color:var(--ink)}
.social{display:flex;gap:5px}
.social span{width:21px;height:21px;border-radius:50%;background:var(--black)}
</style>
</head>
<body>

<div class="topbar abs">
  <div class="info abs" style="left:84px">
    <svg viewBox="0 0 24 24" fill="none" stroke="#222" stroke-width="1.6"><path d="M12 22s7-7 7-12a7 7 0 0 0-14 0c0 5 7 12 7 12z"/><circle cx="12" cy="10" r="2.5"/></svg>
    Gather Your Light Chemin des Vergers 14 Bâtiment B2 1260 Nyon
  </div>
  <div class="info abs" style="left:440px">
    <svg viewBox="0 0 24 24" fill="none" stroke="#222" stroke-width="1.6"><path d="M5 3h4l2 5-3 2a12 12 0 0 0 6 6l2-3 5 2v4a2 2 0 0 1-2 2A17 17 0 0 1 3 5a2 2 0 0 1 2-2z"/></svg>
    +41 21 555 04 82
  </div>
  <div class="info abs" style="left:586px">
    <svg viewBox="0 0 24 24" fill="none" stroke="#222" stroke-width="1.6"><rect x="3" y="5" width="18" height="14"/><path d="M3 6l9 7 9-7"/></svg>
    info@gatheryourlight.ch
  </div>
  <a class="quote-btn abs" href="#">Get a Free Quote Today</a>
</div>

<header class="header abs">
  <div class="logo abs">GATHER<br><span style="font-size:15px;letter-spacing:5px">YOUR LIGHT</span></div>
  <nav class="nav abs">
    <a>Home</a><a>Our Story</a><a>Our Stays</a><a>Activities</a><a>Agenda</a><a>Our Charter</a><a>The Team</a><a>Blog</a><a>Contact Us</a>
  </nav>
</header>

<section class="hero abs" role="img" aria-label="Two smiling friends riding bicycles along a seaside promenade on a sunny day">
  <h1 class="abs">Support your personal development and chase your dream</h1>
  <div class="cta-wrap"><a class="btn" href="#">Contact US</a></div>
</section>

<section class="beige abs">
  <svg class="torn" style="top:-12px" height="26" viewBox="0 0 1200 26" preserveAspectRatio="none"><path fill="#f0ebe3" d="M0 14 L40 10 L80 16 L130 9 L190 15 L240 11 L300 17 L360 10 L420 14 L480 8 L540 15 L600 11 L660 17 L720 10 L780 14 L840 9 L900 16 L960 10 L1020 15 L1080 9 L1140 14 L1200 8 L1200 26 L0 26Z"/></svg>
</section>

<h2 class="h2 abs center" style="top:815px">WHO WE ARE</h2>
<p class="lead abs center" style="top:888px">
Gather Your Light offers well-being and personal growth stays but with a very different spirit.<br>
We’re not a classic wellness brand. Our approach is professional, joyful, and grounded.<br>
We create spaces where people can take a real break — breathe, slow down, and reconnect with themselves.<br>
During our stays, people are welcomed like friends:<br>
with warmth, respect, and no pressure.<br>
Each program combines practices like breathwork, movement, creativity, coaching, and massages in a relaxed,<br>
beautiful setting of the French Alps.
</p>

<div class="photo-wide abs" role="img" aria-label="Dandelion seeds drifting over a meadow at sunset with trees in the background"></div>

<h2 class="h2 abs center" style="top:1566px">WHAT MAKES US DIFFERENT</h2>
<p class="list abs center" style="top:1638px">
A friendly and down-to-earth atmosphere A wide mix of activities.<br>
A mix of inner work and simple pleasures Private rooms, nourishing food, and shared moments<br>
Time to talk, to laugh, to walk, or just be silent together - and feel free to be yourself<br>
Our guests come to pause.<br>
They leave feeling lighter, aligned, and full of life
</p>
<a class="btn small-btn abs" style="left:465px;top:1805px" href="#">REQUEST INFO</a>

<div class="pillar abs" style="left:123px;top:1916px">
  <div class="art" style="background:#f1e8da" role="img" aria-label="Illustration of a soft cloud blowing a breeze"></div>
  <h3>Breathe</h3><div class="rule"></div>
  <p>Lorem Ipsum is simply dummy text of the printing and typesetting industry. Lorem Ipsum has been the industry’s standard dummy it to make a type specimen book.</p>
</div>
<div class="pillar abs" style="left:605px;top:1916px">
  <div class="art" style="background:#f6dcdc" role="img" aria-label="Illustration of a red burst of sparks"></div>
  <h3>Feel</h3><div class="rule"></div>
  <p>Lorem Ipsum is simply dummy text of the printing and typesetting industry. Lorem Ipsum has been the industry’s standard dummy it to make a type specimen book.</p>
</div>
<div class="pillar abs" style="left:123px;top:2166px">
  <div class="art" style="background:#f3d3df" role="img" aria-label="Illustration of a heart made of puzzle pieces"></div>
  <h3>Connect</h3><div class="rule"></div>
  <p>Lorem Ipsum is simply dummy text of the printing and typesetting industry. Lorem Ipsum has been the industry’s standard dummy it to make a type specimen book.</p>
</div>
<div class="pillar abs" style="left:605px;top:2166px">
  <div class="art" style="background:#dcebd6" role="img" aria-label="Illustration of bare feet standing on green grass"></div>
  <h3>Experience</h3><div class="rule"></div>
  <p>Lorem Ipsum is simply dummy text of the printing and typesetting industry. Lorem Ipsum has been the industry’s standard dummy it to make a type specimen book.</p>
</div>

<a class="btn small-btn abs" style="left:465px;top:2435px" href="#">BOOKING REQUEST</a>

<div class="fr abs" style="top:2530px">
<p>Imaginez un espace conçu pour permettre une véritable pause, où chaque souffle compte. A travers ses séjours, Gather Your Light vous invite à un voyage intérieur et extérieur, une expérience unique où chaque étape vous reconnecte à votre vitalité et votre bien-être.</p><br>
<p>Respirez profondément et offrez-vous le luxe de ralentir. Nos programmes sont pensés pour que chaque participant puisse renouer avec le calme et la sérénité.</p><br>
<p>Ressentez chaque sensation, chaque émotion. Grâce à une approche holistique enrichie par des intervenants passionnés, nous combinons des pratiques variées pour éveiller et équilibrer vos cinq sens, en cultivant joie et bienveillance.</p><br>
<p>Connectez pleinement, en petit groupe, dans un cadre chaleureux, humain et respectueux, avec des personnes partageant la même recherche d’épanouissement. C’est aussi une connexion profonde avec soi-même, une opportunité de se redécouvrir dans le confort et le respect de son propre rythme.</p><br>
<p>Expérimentez le changement en profondeur et la richesse de chaque découverte. En explorant de nouvelles pratiques et en vous ouvrant à des perspectives uniques, vous créez votre propre chemin vers une vie joyeuse, équilibrée et pleine de sens.</p><br>
<p>Gather Your Light, c’est faire le choix d’un accompagnement différent : un cocon de bienveillance, un éventail de pratiques et d’expertises, et un cadre conçu pour nourrir l’âme, le corps et l’esprit.</p><br>
<p>Parce que chaque instant est précieux, parce que se reconnecter à la joie et à soi-même est essentiel.</p>
</div>

<section class="blog abs">
  <svg class="torn" style="top:-16px" height="30" viewBox="0 0 1200 30" preserveAspectRatio="none"><path fill="#1a3d99" d="M0 18 L30 10 L70 20 L110 6 L160 18 L200 8 L250 20 L300 9 L350 17 L400 5 L450 18 L500 10 L550 21 L600 7 L650 16 L700 9 L750 20 L800 6 L850 17 L900 10 L950 19 L1000 7 L1050 18 L1100 8 L1150 18 L1200 9 L1200 30 L0 30Z"/></svg>
  <h2 class="abs center">Recent Blog</h2>
  <article class="post abs" style="left:83px">
    <div class="thumb" role="img" aria-label="Woman relaxing in warm sunlight" style="background:linear-gradient(135deg,#d9a778,#8a5a3a)"></div>
    <h4>How meditation is doing our yoga practice better</h4>
    <div class="meta">October 1, 2025 No Comments</div>
    <a class="more">Read More »</a>
  </article>
  <article class="post abs" style="left:436px">
    <div class="thumb" role="img" aria-label="Two people doing partner yoga on a lawn" style="background:linear-gradient(180deg,#c9c3b4 0%,#b7b29b 55%,#6f7b3e 100%)"></div>
    <h4>How meditation is doing our yoga practice better</h4>
    <div class="meta">October 1, 2024 No Comments</div>
    <a class="more">Read More »</a>
  </article>
  <article class="post abs" style="left:785px">
    <div class="thumb" role="img" aria-label="Hands giving a relaxing back massage" style="background:linear-gradient(135deg,#4a3a2e,#c49a7a)"></div>
    <h4>How meditation is doing our yoga practice better</h4>
    <div class="meta">October 1, 2024 No Comments</div>
    <a class="more">Read More »</a>
  </article>
  <svg class="torn" style="top:680px" height="28" viewBox="0 0 1200 28" preserveAspectRatio="none"><path fill="#1a3d99" d="M0 0 L1200 0 L1200 12 L1150 20 L1100 8 L1050 22 L1000 10 L950 19 L900 6 L850 18 L800 10 L750 24 L700 9 L650 18 L600 8 L550 21 L500 11 L450 18 L400 7 L350 20 L300 10 L250 22 L200 8 L150 18 L100 9 L50 20 L0 10Z"/></svg>
</section>

<div class="avatar abs" role="img" aria-label="Portrait of a guest"></div>
<div class="abs center" style="top:4130px;font-size:23px;color:var(--ink)">What others said</div>
<div class="abs center" style="top:4166px;color:var(--star);font-size:19px;letter-spacing:2px">★★★★★</div>
<p class="abs center" style="top:4200px;font-size:14px;line-height:22px;color:var(--ink)">
Lorem ipsum dolor sit amet,  consectetur adipiscing elit, sed do eiusmod tempor incididunt ut labore et<br>
dolore magna aliqua. Lorem ipsum dolor sit amet,  consectetur adipiscing elit, sed do<br>
eiusmod tempor incididunt ut labore et dolore magna aliqua.
</p>
<div class="tname abs center" style="top:4277px">ANNA KELLER</div>
<div class="dots abs"><span></span><span></span><span></span><span class="on"></span></div>

<div class="cta abs">
  <div class="phone">+41 21 555 04 82</div>
  <p>Ready to schedule your cleanup or have questions?<br>We’d love to hear from you.</p>
</div>

<footer class="footer abs">
  <svg class="torn" style="top:-14px" height="26" viewBox="0 0 1200 26" preserveAspectRatio="none"><path fill="#0b0b0b" d="M0 10 L40 16 L90 6 L140 15 L200 9 L260 17 L1000 14 L1040 8 L1090 16 L1140 7 L1200 14 L1200 26 L0 26Z"/></svg>
  <div class="fcol abs" style="left:98px;top:136px">
    <h5>Information</h5>
    <ul><li>- Home</li><li>- Our Story</li><li>- Our Stays</li><li>- Activities</li></ul>
  </div>
  <div class="fcol abs" style="left:303px;top:136px">
    <h5>About</h5>
    <ul><li>- Agenda</li><li>- Our Charter</li><li>- The Team</li><li>- Contact</li><li>- Blog</li></ul>
  </div>
  <div class="fcol fcontact abs" style="left:482px;top:136px">
    <h5>Contact us</h5>
    <div style="margin-top:36px;font-weight:600;font-size:15px"><svg viewBox="0 0 24 24" fill="none" stroke="#fff" stroke-width="1.6"><path d="M5 3h4l2 5-3 2a12 12 0 0 0 6 6l2-3 5 2v4a2 2 0 0 1-2 2A17 17 0 0 1 3 5a2 2 0 0 1 2-2z"/></svg>+41 21 555 04 82</div>
    <div><svg viewBox="0 0 24 24" fill="none" stroke="#fff" stroke-width="1.6"><rect x="3" y="5" width="18" height="14"/><path d="M3 6l9 7 9-7"/></svg>info@gatheryourlight.ch</div>
    <div style="line-height:17px"><svg viewBox="0 0 24 24" fill="none" stroke="#fff" stroke-width="1.6"><path d="M12 22s7-7 7-12a7 7 0 0 0-14 0c0 5 7 12 7 12z"/><circle cx="12" cy="10" r="2.5"/></svg><span>Gather Your Light Sàrl<br>Chemin des Vergers 14<br>Bâtiment B2<br>CH – 1260 Nyon</span></div>
  </div>
  <div class="flogo abs" style="left:762px;top:144px">Gather Your Light</div>
  <div class="subscribe abs" style="left:760px;top:256px">Subscribe to our newsletter</div>
  <div class="field abs" style="left:762px;top:298px"><span>Email</span></div>
  <div class="fine abs" style="left:762px;top:340px">Subscribe today and get exciting gifts and 10% off on your first order.</div>
</footer>

<a class="quote-tab abs" href="#">CLICK HERE FOR A<br>FREE QUOTE!</a>

<div class="bottom abs">
  <div class="abs" style="left:84px;top:8px">© 2025 Gather Your Light</div>
  <div class="abs" style="left:932px;top:4px;display:flex;align-items:center;gap:6px">Follow me: <div class="social"><span></span><span></span><span></span><span></span></div></div>
</div>

</body>
</html>
```